IT services company needs a business card designed

-2 sided business card.-Front is going to be the logo raised (3D floating effect) on a black background. Make the logos spider web shiny silver and keep the spider the same design. -Back needs to have the following information:Darrel Sotho, Managing Partner, Cell: 738-402-1954, Website: Plankhorn.com, Email: Darrel@Plankhorn.com
Target Market(s)
IT Services
Industry/Entity Type
It Company
Contact Information for Business Card
-2 sided business card.
-Front is going to be the logo raised (3D floating effect) on a black background. Make the logos spider web shiny silver and keep the spider the same design.
-Back needs to have the following information:
Darrel Sotho, Managing Partner, Cell: 738-402-1954, Website: Plankhorn.com, Email: Darrel@Plankhorn.com

```html
<!DOCTYPE html>
<html lang="en">
<head>
<meta charset="utf-8">
<title>Plankhorn – Business Card</title>
<link rel="stylesheet" href="https://fonts.googleapis.com/css2?family=Open+Sans:wght@400;600;700&display=swap">
<style>
  :root {
    --backdrop: #1b1b1c;
    --card: #232324;
    --card-edge: #2c2c2d;
    --silver: #cfd1d3;
    --silver-dim: #9a9c9e;
    --accent: #1aa3de;
    --icon-ink: #2a2a2b;
  }
  * { box-sizing: border-box; margin: 0; padding: 0; }
  html, body {
    width: 1200px; height: 900px; overflow: hidden;
    background: var(--backdrop);
    font-family: "Open Sans", Arial, sans-serif;
  }
  .sheet {
    width: 1200px; height: 900px;
    display: flex; flex-direction: column;
    align-items: center; justify-content: center; gap: 36px;
  }
  .card {
    width: 680px; height: 390px;
    background: radial-gradient(ellipse at 40% 35%, var(--card-edge), var(--card) 70%);
    box-shadow: 0 14px 30px rgba(0,0,0,.55);
    position: relative;
  }
  /* front */
  .card--front { display: flex; align-items: center; justify-content: center; }
  .brand { display: flex; align-items: center; gap: 16px; }
  .brand__dot { width: 22px; height: 22px; border-radius: 50%; background: var(--accent); }
  .brand__name {
    font-weight: 600; font-size: 52px; letter-spacing: 4px;
    color: var(--silver); text-transform: uppercase;
  }
  /* back */
  .card--back { display: flex; flex-direction: column; align-items: center; justify-content: center; }
  .holder { text-align: center; }
  .holder__name {
    font-weight: 700; font-size: 34px; letter-spacing: 1px;
    text-transform: uppercase; color: var(--silver); line-height: 1.1;
  }
  .holder__first { color: var(--accent); }
  .holder__role {
    font-size: 13px; letter-spacing: 2px; text-transform: uppercase;
    color: var(--silver); margin-top: 4px;
  }
  .contact-icons { display: flex; gap: 18px; margin: 26px 0 20px; }
  .contact-icon { width: 34px; height: 34px; display: block; }
  .contact-lines { text-align: center; }
  .contact-lines li {
    list-style: none; font-size: 20px; color: var(--silver);
    letter-spacing: .5px; line-height: 1.4;
  }
</style>
</head>
<body>
<main class="sheet">

  <section class="card card--front" aria-label="Card front">
    <div class="brand">
      <span class="brand__dot"></span>
      <span class="brand__name">Plankhorn</span>
    </div>
  </section>

  <section class="card card--back" aria-label="Card back">
    <div class="holder">
      <h1 class="holder__name"><span class="holder__first">Darrel</span> Sotho</h1>
      <p class="holder__role">Managing Partner</p>
    </div>

    <svg width="0" height="0" style="position:absolute">
      <defs>
        <radialGradient id="chrome" cx="40%" cy="35%" r="70%">
          <stop offset="0" stop-color="#f4f5f6"/>
          <stop offset=".6" stop-color="#b9bbbd"/>
          <stop offset="1" stop-color="#7d7f81"/>
        </radialGradient>
      </defs>
    </svg>

    <div class="contact-icons">
      <svg class="contact-icon" viewBox="0 0 34 34" aria-label="Phone">
        <circle cx="17" cy="17" r="16" fill="url(#chrome)"/>
        <path d="M13 9c1 0 2 3 2 4s-1.5 1.3-1.2 2.3c.6 1.8 2 3.5 3.8 4.4 1 .4 1.4-1.2 2.3-1.2s3.6 1.3 3.6 2.3c0 1.5-1.6 2.7-3 2.7-5 0-10.5-5.5-10.5-10.5 0-1.5 1.5-4 3-4z" fill="var(--icon-ink)"/>
      </svg>
      <svg class="contact-icon" viewBox="0 0 34 34" aria-label="Email">
        <circle cx="17" cy="17" r="16" fill="url(#chrome)"/>
        <rect x="9" y="11.5" width="16" height="11" rx="1" fill="none" stroke="var(--icon-ink)" stroke-width="1.8"/>
        <path d="M9.5 12l7.5 6 7.5-6" fill="none" stroke="var(--icon-ink)" stroke-width="1.8"/>
      </svg>
      <svg class="contact-icon" viewBox="0 0 34 34" aria-label="Website">
        <circle cx="17" cy="17" r="16" fill="url(#chrome)"/>
        <g fill="none" stroke="var(--icon-ink)" stroke-width="1.5">
          <circle cx="17" cy="17" r="8"/>
          <ellipse cx="17" cy="17" rx="3.5" ry="8"/>
          <path d="M9 17h16M10.5 13h13M10.5 21h13"/>
        </g>
      </svg>
    </div>

    <ul class="contact-lines">
      <li>738-402-1954</li>
      <li>Darrel@Plankhorn.com</li>
      <li>www.Plankhorn.com</li>
    </ul>
  </section>

</main>
</body>
</html>
```